*YO!!! Designers Needed!!* Front Page Cover Needed for a $$Billion Dollar$$ Company

We are a manufacturer of aluminum electrolytic capacitors. We are looking to create a front page cover that will be used on our annual report. We are a publicly listed company and work with many Pinnacle 300 companies, so your work will be viewed by the BIG GUNS and EXECUTIVES around the WORLD! If selected, you may be selected for additional work.

The front page cover should be unique. If elegance, modern, bling, and creativity somehow got together and had a child, that's what the cover page would look like!

Inspired Examples attached. Check them out!

www.velmoro.com

Font styles to use
Sans Serif

Requirements
Must have
• 1. Must include the attached logo. Logo size, color, and placement are at your discretion.

2. Should include the text, '2020 Annual Report'

3. The design should incorporate the use of foil and/or be embossed. The foil can be part of the design or can be the full page. See various examples attached for reference.

4. Shall be in A4 size and vertical orientation.
Nice to have
• Feel free to add any icons or stock photos (for example capacitors or circuit boards) if needed.

Be creative here and don't be afraid to be bold! The end product will be printed and budget is not a limiting factor, so feel free to make it extravagant if needed.

Our slogan is "Think Ahead". This slogan can or cannot be part of the theme.

```html
<!DOCTYPE html>
<html lang="en">
<head>
<meta charset="utf-8">
<title>Velmoro Annual Report 2020 Cover</title>
<link href="https://fonts.googleapis.com/css2?family=Montserrat:wght@200;400;600;700&display=swap" rel="stylesheet">
<style>
  :root {
    --page-bg: #ffffff;
    --navy-light: #033c70;
    --navy-mid: #03285e;
    --navy-deep: #020a3d;
    --slate: #566a82;
    --gold: #c9a45c;
    --white: #ffffff;
  }
  * { margin: 0; padding: 0; box-sizing: border-box; }
  html, body {
    width: 1200px;
    height: 1200px;
    overflow: hidden;
    background: var(--page-bg);
    font-family: "Montserrat", sans-serif;
  }
  .canvas {
    position: relative;
    width: 1200px;
    height: 1200px;
  }
  .cover {
    position: absolute;
    left: 228px;
    top: 92px;
    width: 743px;
    height: 1016px;
    overflow: hidden;
  }
  .cover-texture {
    position: absolute;
    inset: 0;
    background: linear-gradient(90deg, var(--navy-light) 0%, var(--navy-mid) 50%, var(--navy-light) 100%);
  }
  .cover-shapes {
    position: absolute;
    inset: 0;
    width: 743px;
    height: 1016px;
  }
  .brand-name {
    font-family: "Montserrat", sans-serif;
    font-weight: 700;
    font-size: 37px;
    letter-spacing: 1px;
    fill: var(--gold);
  }
  .brand-slogan {
    font-family: "Montserrat", sans-serif;
    font-weight: 600;
    font-size: 11px;
    letter-spacing: 0.6px;
    fill: var(--white);
  }
  .report-title {
    font-family: "Montserrat", sans-serif;
    font-weight: 200;
    font-size: 20px;
    fill: var(--white);
  }
  .report-year {
    font-family: "Montserrat", sans-serif;
    font-weight: 400;
    font-size: 20px;
    fill: var(--white);
  }
</style>
</head>
<body>
<main class="canvas">
  <section class="cover">
    <div class="cover-texture" role="img" aria-label="Embossed navy blue pattern of right-pointing triangles covering the page"></div>
    <svg class="cover-shapes" viewBox="0 0 743 1016" xmlns="http://www.w3.org/2000/svg">
      <defs>
        <linearGradient id="arrow-dark" x1="0" y1="0" x2="1" y2="0">
          <stop offset="0" stop-color="#03265c"/>
          <stop offset="0.6" stop-color="#030c44"/>
          <stop offset="1" stop-color="#020a3d"/>
        </linearGradient>
      </defs>
      <polygon class="arrow-brand" points="210,330 524,508 210,684" fill="url(#arrow-dark)" stroke="#0a3470" stroke-width="1"/>
      <polygon class="arrow-report" points="532,394 739,508 532,622" fill="var(--slate)" stroke="#0a3470" stroke-width="1"/>

      <text class="brand-name" x="327" y="520" text-anchor="middle">VELMORO</text>
      <text class="brand-slogan" x="430" y="546" text-anchor="end">LEAD FORWARD.</text>

      <g transform="translate(572 508) rotate(-90)">
        <text class="report-title" x="0" y="0" text-anchor="middle">Annual Report</text>
        <text class="report-year" x="0" y="25" text-anchor="middle">2020</text>
      </g>
    </svg>
  </section>
</main>
</body>
</html>
```